Preoperative Medical clearance for Patients on blood thinners

Prepare a flow chart which directs medical office staff to properly triage patients preparing for surgery who are on blood thinners. We will provide a rudimentary flow chart with all necessary information. We need a better layout which is more appealing and intuitive.

Target Market(s)

internal office use

Industry/Entity Type

Medical

Font styles to use
Sans Serif

Requirements
Must have
• attractive, intuitive layout
Should not have
• things that promote confusion

```html
<!DOCTYPE html>
<html lang="en">
<head>
<meta charset="utf-8">
<title>Preoperative Clearance – Patients on Blood Thinners</title>
<link rel="stylesheet" href="https://fonts.googleapis.com/css2?family=Montserrat:wght@400;600;700&family=Schoolbell&display=swap">
<style>
  :root{
    --yes:#00c800;
    --yes-dark:#0a5e0a;
    --no:#e00000;
    --no-dark:#6b0000;
    --band:#ffff00;
    --head:#f75000;
    --bar:#000000;
    --ink:#111111;
    --ink-red:#7a0000;
    --white:#ffffff;
  }
  html,body{margin:0;padding:0;width:1158px;height:1200px;overflow:hidden;background:#8a8d90;}
  .chart{display:block;width:1158px;height:1200px;font-family:"Montserrat",sans-serif;}
  .title{font-family:"Schoolbell",cursive;font-size:96px;fill:var(--white);}
  .badge-text{font-weight:700;fill:var(--white);text-anchor:middle;}
  .or-text{font-weight:600;fill:var(--white);font-size:46px;}
  .band{fill:var(--band);}
  .band-text{font-weight:700;font-size:38px;fill:var(--ink);text-anchor:middle;}
  .section-head{fill:var(--head);}
  .section-text{font-weight:700;font-size:32px;fill:var(--white);text-anchor:middle;letter-spacing:1px;}
  .question-bar{fill:var(--bar);}
  .question-text{font-weight:600;font-size:27px;fill:var(--white);text-anchor:middle;}
  .btn-yes{fill:var(--yes);stroke:var(--yes-dark);stroke-width:3;}
  .btn-no{fill:var(--no);stroke:var(--no-dark);stroke-width:3;}
  .btn-text{font-weight:700;font-size:27px;fill:var(--white);text-anchor:middle;}
  .btn-text.small{font-size:23px;}
  .taper-yes{fill:var(--yes-dark);}
  .taper-no{fill:var(--no-dark);}
  .link-yes{fill:var(--white);stroke:var(--yes-dark);stroke-width:2;}
  .link-no{fill:var(--white);stroke:var(--no-dark);stroke-width:2;}
  .box-action{fill:var(--band);stroke:var(--ink);stroke-width:3;}
  .box-yes{fill:var(--white);stroke:var(--yes-dark);stroke-width:3;}
  .box-no{fill:var(--white);stroke:var(--no-dark);stroke-width:3;}
  .step{font-size:18.5px;fill:var(--ink);text-anchor:middle;letter-spacing:.3px;}
  .step.ask{fill:var(--ink-red);}
</style>
</head>
<body>
<svg class="chart" viewBox="0 0 1448 1500" xmlns="http://www.w3.org/2000/svg">
  <defs>
    <linearGradient id="sceneTop" x1="0" y1="0" x2="1" y2="0">
      <stop offset="0" stop-color="#6f7780"/>
      <stop offset=".6" stop-color="#7c848d"/>
      <stop offset=".8" stop-color="#3a5f9a"/>
      <stop offset="1" stop-color="#2f5a9c"/>
    </linearGradient>
    <linearGradient id="sceneBottom" x1="0" y1="0" x2="0" y2="1">
      <stop offset="0" stop-color="#b7b9bb"/>
      <stop offset=".5" stop-color="#8e9092"/>
      <stop offset="1" stop-color="#a9abad"/>
    </linearGradient>
  </defs>

  <g class="backdrop" role="img" aria-label="Blurred hospital corridor with a surgeon in blue scrubs, arms crossed">
    <rect x="0" y="0" width="1448" height="627" fill="url(#sceneTop)"/>
    <rect x="0" y="627" width="1448" height="873" fill="url(#sceneBottom)"/>
  </g>

  <!-- Heading -->
  <text class="title" x="95" y="238">Patient taking a</text>
  <text class="title" x="95" y="342">blood thinner?</text>
  <circle cx="1010" cy="258" r="90" fill="var(--yes)"/>
  <text class="badge-text" x="1010" y="283" font-size="50">YES</text>
  <text class="or-text" x="1128" y="278">or</text>
  <circle cx="1277" cy="262" r="65" fill="var(--no)"/>
  <text class="badge-text" x="1275" y="280" font-size="44">NO</text>

  <rect class="band" x="27" y="410" width="1392" height="114"/>
  <text class="band-text" x="716" y="484">Cardiac problem, Bleeding Disorder, or Stroke?</text>

  <!-- Section headers -->
  <rect class="section-head" x="57" y="595" width="404" height="73"/>
  <text class="section-text" x="253" y="646">CARDIAC</text>
  <rect class="section-head" x="515" y="595" width="870" height="73"/>
  <text class="section-text" x="955" y="645">STROKE / BLEEDING DISORDER</text>

  <!-- Column: Cardiology -->
  <g class="pathway" transform="translate(57 0)">
    <rect class="question-bar" x="0" y="668" width="404" height="72"/>
    <text class="question-text" x="202" y="716">Have a cardiologist?</text>

    <rect class="btn-yes" x="2" y="742" width="182" height="70"/>
    <text class="btn-text" x="93" y="788">YES</text>
    <polygon class="taper-yes" points="2,812 184,812 110,845 76,845"/>
    <rect class="link-yes" x="87" y="843" width="12" height="28"/>
    <rect class="box-action" x="2" y="870" width="182" height="114"/>
    <text class="step" x="93" y="912">Refer to</text>
    <text class="step" x="93" y="934">Patient’s current</text>
    <text class="step" x="93" y="956">cardiologist</text>

    <rect class="btn-no" x="220" y="742" width="183" height="70"/>
    <text class="btn-text" x="312" y="788">NO</text>
    <polygon class="taper-no" points="220,812 403,812 330,845 294,845"/>
    <rect class="link-no" x="306" y="843" width="12" height="28"/>
    <rect class="box-no" x="220" y="870" width="183" height="114"/>
    <text class="step ask" x="312" y="912">Have a</text>
    <text class="step ask" x="312" y="934">primary care</text>
    <text class="step ask" x="312" y="956">doctor?</text>
    <polygon class="taper-no" points="220,984 403,984 330,1012 294,1012"/>
    <rect class="link-no" x="306" y="1010" width="12" height="52"/>

    <rect class="btn-yes" x="218" y="1060" width="93" height="72"/>
    <text class="btn-text small" x="264" y="1106">YES</text>
    <rect class="btn-no" x="313" y="1060" width="88" height="72"/>
    <text class="btn-text small" x="357" y="1106">NO</text>
    <polygon class="taper-yes" points="218,1062 218,1130 198,1096"/>
    <rect class="link-yes" x="182" y="1090" width="18" height="12"/>
    <polygon class="taper-no" points="313,1132 401,1132 372,1160 348,1160"/>
    <rect class="link-no" x="354" y="1158" width="12" height="44"/>

    <rect class="box-yes" x="-4" y="1042" width="186" height="113"/>
    <text class="step" x="89" y="1076">Call primary</text>
    <text class="step" x="89" y="1097">and ask for</text>
    <text class="step" x="89" y="1118">preffered</text>
    <text class="step" x="89" y="1139">cardiologist.</text>
    <polygon class="taper-yes" points="-4,1155 182,1155 110,1182 68,1182"/>
    <rect class="link-yes" x="82" y="1180" width="12" height="22"/>

    <rect class="box-yes" x="-4" y="1200" width="185" height="113"/>
    <text class="step" x="88" y="1230">Refer to</text>
    <text class="step" x="88" y="1251">cardiologist</text>
    <text class="step" x="88" y="1272">selected by</text>
    <text class="step" x="88" y="1293">primary</text>
    <polygon class="taper-yes" points="-4,1313 181,1313 181,1315 -4,1362"/>

    <rect class="box-no" x="216" y="1200" width="187" height="113"/>
    <text class="step" x="310" y="1245">Select specialist</text>
    <text class="step" x="310" y="1266">and refer to</text>
    <text class="step" x="310" y="1287">establish care</text>
    <polygon class="taper-no" points="216,1313 403,1313 403,1362 216,1315"/>
  </g>

  <!-- Column: Neurology -->
  <g class="pathway" transform="translate(515 0)">
    <rect class="question-bar" x="0" y="668" width="406" height="72"/>
    <text class="question-text" x="203" y="716">Have a neurologist?</text>

    <rect class="btn-yes" x="2" y="742" width="182" height="70"/>
    <text class="btn-text" x="93" y="788">YES</text>
    <polygon class="taper-yes" points="2,812 184,812 110,845 76,845"/>
    <rect class="link-yes" x="87" y="843" width="12" height="28"/>
    <rect class="box-action" x="2" y="870" width="182" height="114"/>
    <text class="step" x="93" y="912">Refer to</text>
    <text class="step" x="93" y="934">Patient’s current</text>
    <text class="step" x="93" y="956">neurologist</text>

    <rect class="btn-no" x="222" y="742" width="183" height="70"/>
    <text class="btn-text" x="314" y="788">NO</text>
    <polygon class="taper-no" points="222,812 405,812 332,845 296,845"/>
    <rect class="link-no" x="308" y="843" width="12" height="28"/>
    <rect class="box-no" x="222" y="870" width="183" height="114"/>
    <text class="step ask" x="314" y="912">Have a</text>
    <text class="step ask" x="314" y="934">primary care</text>
    <text class="step ask" x="314" y="956">doctor?</text>
    <polygon class="taper-no" points="222,984 405,984 332,1012 296,1012"/>
    <rect class="link-no" x="308" y="1010" width="12" height="52"/>

    <rect class="btn-yes" x="222" y="1060" width="92" height="72"/>
    <text class="btn-text small" x="268" y="1106">YES</text>
    <rect class="btn-no" x="316" y="1060" width="88" height="72"/>
    <text class="btn-text small" x="359" y="1106">NO</text>
    <polygon class="taper-yes" points="222,1062 222,1130 202,1096"/>
    <rect class="link-yes" x="184" y="1090" width="20" height="12"/>
    <polygon class="taper-no" points="316,1132 404,1132 375,1160 351,1160"/>
    <rect class="link-no" x="357" y="1158" width="12" height="44"/>

    <rect class="box-yes" x="-2" y="1042" width="186" height="113"/>
    <text class="step" x="96" y="1076">Call primary</text>
    <text class="step" x="96" y="1097">and ask for</text>
    <text class="step" x="96" y="1118">preffered</text>
    <text class="step" x="96" y="1139">neurologist.</text>
    <polygon class="taper-yes" points="-2,1155 184,1155 110,1182 70,1182"/>
    <rect class="link-yes" x="84" y="1180" width="12" height="18"/>

    <rect class="box-yes" x="-2" y="1196" width="185" height="113"/>
    <text class="step" x="92" y="1230">Refer to</text>
    <text class="step" x="92" y="1251">neurologist</text>
    <text class="step" x="92" y="1272">selected by</text>
    <text class="step" x="92" y="1293">primary</text>
    <polygon class="taper-yes" points="-2,1309 183,1309 183,1311 -2,1358"/>

    <rect class="box-no" x="220" y="1200" width="185" height="113"/>
    <text class="step" x="313" y="1245">Select specialist</text>
    <text class="step" x="313" y="1266">and refer to</text>
    <text class="step" x="313" y="1287">establish care</text>
    <polygon class="taper-no" points="220,1313 405,1313 405,1362 220,1315"/>
  </g>

  <!-- Column: Hematology -->
  <g class="pathway" transform="translate(979 0)">
    <rect class="question-bar" x="0" y="668" width="406" height="72"/>
    <text class="question-text" x="203" y="716">Have a hematologist?</text>

    <rect class="btn-yes" x="2" y="742" width="182" height="70"/>
    <text class="btn-text" x="88" y="788">YES</text>
    <polygon class="taper-yes" points="2,812 184,812 110,845 76,845"/>
    <rect class="link-yes" x="87" y="843" width="12" height="28"/>
    <rect class="box-action" x="2" y="870" width="182" height="114"/>
    <text class="step" x="93" y="911">Refer to</text>
    <text class="step" x="93" y="933">hematologist</text>
    <text class="step" x="93" y="954">for clearance</text>

    <rect class="btn-no" x="222" y="742" width="183" height="70"/>
    <text class="btn-text" x="318" y="788">NO</text>
    <polygon class="taper-no" points="222,812 405,812 332,845 296,845"/>
    <rect class="link-no" x="311" y="843" width="12" height="26"/>
    <rect class="box-no" x="222" y="868" width="183" height="116"/>
    <text class="step ask" x="316" y="911">Have a</text>
    <text class="step ask" x="316" y="933">primary care</text>
    <text class="step ask" x="316" y="955">doctor?</text>
    <polygon class="taper-no" points="222,984 405,984 332,1012 296,1012"/>
    <rect class="link-no" x="311" y="1010" width="12" height="52"/>

    <rect class="btn-yes" x="222" y="1060" width="92" height="72"/>
    <text class="btn-text small" x="267" y="1106">YES</text>
    <rect class="btn-no" x="316" y="1060" width="88" height="72"/>
    <text class="btn-text small" x="359" y="1106">NO</text>
    <polygon class="taper-yes" points="222,1062 222,1130 202,1096"/>
    <rect class="link-yes" x="184" y="1090" width="20" height="12"/>
    <polygon class="taper-no" points="316,1132 404,1132 375,1160 351,1160"/>
    <rect class="link-no" x="356" y="1158" width="12" height="44"/>

    <rect class="box-yes" x="0" y="1042" width="184" height="113"/>
    <text class="step" x="92" y="1076">Call primary</text>
    <text class="step" x="92" y="1097">and ask for</text>
    <text class="step" x="93" y="1118">preffered</text>
    <text class="step" x="92" y="1139">hematologist.</text>
    <polygon class="taper-yes" points="0,1155 184,1155 110,1182 72,1182"/>
    <rect class="link-yes" x="86" y="1180" width="12" height="22"/>

    <rect class="box-yes" x="0" y="1200" width="184" height="113"/>
    <text class="step" x="92" y="1230">Refer to</text>
    <text class="step" x="92" y="1251">hematologist</text>
    <text class="step" x="92" y="1272">selected by</text>
    <text class="step" x="92" y="1293">primary</text>
    <polygon class="taper-yes" points="0,1313 184,1313 184,1315 0,1362"/>

    <rect class="box-no" x="220" y="1200" width="186" height="113"/>
    <text class="step" x="315" y="1246">Selet specialist</text>
    <text class="step" x="315" y="1267">and refer to</text>
    <text class="step" x="315" y="1288">establish care</text>
    <polygon class="taper-no" points="220,1313 406,1313 406,1362 220,1315"/>
  </g>
</svg>
</body>
</html>
```